Letterhead and business card design

We have recently had a logo designed by tarnvalehub. now we need a corporate identity with business card and lettehead design.

Target Market(s)

law firms corporates

Industry/Entity Type

Business

Requirements
Should not have
• cheesy detecive stuff like magnifying glasses etxcc

```html
<!DOCTYPE html>
<html lang="en">
<head>
<meta charset="utf-8">
<title>Halvorsen &amp; Kemp – Business Card</title>
<link rel="stylesheet" href="https://fonts.googleapis.com/css2?family=Lato:wght@400&display=swap">
<style>
  :root {
    --stage: #3b3b3b;
    --card-front: #ffffff;
    --card-back-top: #4a5858;
    --card-back-bottom: #364343;
    --ink: #5a5d5e;
    --ink-soft: #7b7f80;
    --rule: #8c9091;
    --back-ink: #27302f;
  }
  * { margin: 0; padding: 0; box-sizing: border-box; }
  html, body { width: 1200px; height: 900px; overflow: hidden; }
  body {
    background: var(--stage);
    display: flex;
    flex-direction: column;
    align-items: center;
    justify-content: center;
    gap: 40px;
    font-family: "Lato", sans-serif;
  }
  .card {
    width: 700px;
    height: 400px;
    position: relative;
    box-shadow: 0 10px 30px rgba(0,0,0,0.35);
  }
  .card--front { background: var(--card-front); color: var(--ink); }
  .card--back {
    background: linear-gradient(160deg, var(--card-back-top), var(--card-back-bottom));
    display: flex;
    align-items: center;
    justify-content: center;
  }
  .brand-name {
    font-family: "Lato", sans-serif;
    font-weight: 400;
    font-size: 34px;
    letter-spacing: 2px;
    text-transform: uppercase;
    line-height: 1;
    white-space: nowrap;
  }
  .card--front .brand-name {
    position: absolute;
    top: 62px;
    right: 48px;
    color: var(--ink);
  }
  .card--back .brand-name { color: var(--back-ink); }
  .holder {
    position: absolute;
    top: 172px;
    right: 150px;
    text-align: center;
    color: var(--ink);
  }
  .holder__name { font-size: 20px; letter-spacing: 0.5px; text-transform: uppercase; }
  .holder__title { font-size: 15px; color: var(--ink-soft); margin-top: 2px; }
  .contact {
    position: absolute;
    font-size: 15px;
    line-height: 1.45;
    color: var(--ink);
  }
  .contact dl { display: grid; grid-template-columns: 64px auto; }
  .contact dt { color: var(--ink-soft); }
  .contact--personal { left: 48px; top: 140px; }
  .divider {
    position: absolute;
    left: 48px;
    right: 48px;
    top: 262px;
    height: 1px;
    background: var(--rule);
  }
  .contact--office { right: 48px; top: 290px; }
</style>
</head>
<body>
  <section class="card card--front" aria-label="Business card front">
    <div class="brand-name">Halvorsen &amp; Kemp</div>
    <div class="contact contact--personal">
      <dl>
        <dt>Mobile:</dt><dd>+64 21 555 0147</dd>
        <dt>Email:</dt><dd>marcus@hkinquiries.co.nz</dd>
      </dl>
    </div>
    <div class="holder">
      <div class="holder__name">Marcus Halvorsen</div>
      <div class="holder__title">Director</div>
    </div>
    <div class="divider"></div>
    <div class="contact contact--office">
      <dl>
        <dt>Phone:</dt><dd>+64 9 555 0132</dd>
        <dt>Fax:</dt><dd>+64 9 555 0178</dd>
      </dl>
    </div>
  </section>

  <section class="card card--back" aria-label="Business card back">
    <div class="brand-name">Halvorsen &amp; Kemp</div>
  </section>
</body>
</html>
```